Business Card Design

We offer Procurement, Supply Chain, Merchandise Expediting, Customs Management, Shipping Documentation and many other Specialized Consultancies. The many products we handle are used in many different industries like Oil, Gas and Drilling Hardware, Construction Equipment, Industrial Parts and much more.
Our Slogan is:
"We look from around the world for what you need, bringing it to your door in the shortest possible time with the best all inclusive price"

Target Market(s)

US Export companies, Mexican Import companies and others companies that are looking for Oil & Gas products

Industry/Entity Type

Business

Contact Information for Business Card

Corvinet Trade Partners & Providers, LLC
Phone: +1 (281) 555-0193
31542 Larkfield Pkwy, Ste 1800
Katy, Texas 77000 USA
www.corvinet.biz

Font styles to use
Other font styles liked:
• Century Gothic

```html
<!DOCTYPE html>
<html lang="en">
<head>
<meta charset="utf-8">
<title>Corvinet Business Card</title>
<link rel="stylesheet" href="https://fonts.googleapis.com/css2?family=Questrial&display=swap">
<style>
  :root {
    --brand-green: #0b6b3f;
    --brand-red: #e83e4a;
    --ink: #2a2a2a;
    --card: #ffffff;
    --backdrop: #e9e6e1;
    --label: #6f6a63;
    --card-edge: #d4d0ca;
  }
  * { margin: 0; padding: 0; box-sizing: border-box; }
  html, body {
    width: 1001px; height: 1200px; overflow: hidden;
    background: var(--backdrop);
    font-family: "Questrial", "Century Gothic", sans-serif;
  }
  .sheet { position: relative; width: 1001px; height: 1200px; }
  .side-label {
    position: absolute; left: 0; width: 100%;
    text-align: center; color: var(--label);
    font-size: 46px; letter-spacing: 1px;
  }
  .side-label--front { top: 22px; }
  .side-label--back { top: 1108px; }
  .card {
    position: absolute; width: 810px; height: 463px;
    background: var(--card);
    border: 1px solid var(--card-edge);
  }
  .card--front { left: 66px; top: 99px; }
  .card--back { left: 77px; top: 598px; }
  .edge-bar { position: absolute; left: 0; width: 16px; }
  .edge-bar--green { top: 0; height: 230px; background: var(--brand-green); }
  .edge-bar--red { top: 230px; bottom: 0; background: var(--brand-red); }
  .brand {
    position: absolute; left: 69px; top: 51px;
    display: flex; align-items: center; gap: 18px;
  }
  .brand-square {
    width: 106px; height: 106px; border-radius: 14px;
    background: var(--brand-red);
  }
  .brand-name {
    font-size: 112px; line-height: 1; color: var(--brand-green);
    letter-spacing: -1px;
  }
  .contact-line {
    position: absolute; left: 69px;
    display: flex; align-items: center; gap: 10px;
    font-size: 21px; color: var(--ink); white-space: nowrap;
  }
  .contact-line svg { width: 20px; height: 20px; flex: none; }
  .contact-line--phone { top: 245px; }
  .contact-line--web { top: 293px; }
  .company-name {
    position: absolute; left: 69px; top: 350px;
    font-size: 21px; color: var(--brand-red); white-space: nowrap;
  }
  .contact-line--address { top: 393px; }
  .back-mark {
    position: absolute; left: 258px; top: 82px;
    width: 293px; height: 297px; border-radius: 30px;
    background: var(--brand-red);
    display: flex; align-items: center; justify-content: center;
  }
  .back-mark-name { font-size: 54px; color: var(--card); }
</style>
</head>
<body>
<main class="sheet">
  <div class="side-label side-label--front">FRONT</div>

  <section class="card card--front" aria-label="Card front">
    <div class="edge-bar edge-bar--green"></div>
    <div class="edge-bar edge-bar--red"></div>

    <div class="brand">
      <div class="brand-square"></div>
      <div class="brand-name">corvinet</div>
    </div>

    <div class="contact-line contact-line--phone">
      <svg viewBox="0 0 20 20" aria-hidden="true"><path fill="#0b6b3f" d="M5 1h3l1 5-2 1.5c.8 2.3 2 4 3.5 5.5L12 11l5 1v3c0 1.5-1.2 2.5-2.6 2.3C8 16.3 3.4 11.2 2.7 4.8 2.5 2.5 3.5 1 5 1z"/></svg>
      <span>+1 (281) 555-0193 31542</span>
    </div>

    <div class="contact-line contact-line--web">
      <svg viewBox="0 0 20 20" aria-hidden="true"><g fill="none" stroke="#0b6b3f" stroke-width="1.6"><circle cx="10" cy="10" r="8.2"/><ellipse cx="10" cy="10" rx="3.6" ry="8.2"/><path d="M2 10h16M3.5 5.5h13M3.5 14.5h13"/></g></svg>
      <span>www.corvinet.biz</span>
    </div>

    <div class="company-name">Corvinet Trade Partners &amp; Providers, LLC</div>

    <div class="contact-line contact-line--address">
      <svg viewBox="0 0 20 20" aria-hidden="true"><path fill="#0b6b3f" d="M10 2 1 10h3v8h5v-5h2v5h5v-8h3z"/></svg>
      <span>Larkfield Pkwy, Ste 1800 Katy, Texas 77000 USA</span>
    </div>
  </section>

  <section class="card card--back" aria-label="Card back">
    <div class="back-mark"><span class="back-mark-name">corvinet</span></div>
  </section>

  <div class="side-label side-label--back">BACK</div>
</main>
</body>
</html>
```